QLM Packaging design for beauty industry

Looking for my first product packaging design, tailored to reflect QLM’s branding and product benefits, along with mockup suggestions to bring it to life.

---

Front of the Box Copy
**Header**:
QLM Veloria Air Stand-Up Dryer

**Subheader**:
Effortless Styling. Professional Results.

**Features (Use Icons + Text)**:
- **Adjustable Height**: Perfect for all users and settings.
- **Ionic Technology**: Faster drying, frizz-free results.
- **360° Heat Distribution**: Even styling every time.
- **Lightweight & Portable**: Easy to move and assemble.

**Call to Action (CTA)**:
*“Empower Your Beauty with QLM Professional-Grade Tools.”*

---

### **Side Panel Copy**
**About QLM**:
"At QLM, we believe beauty is power. Our tools are designed with precision, ensuring every style feels as beautiful as you are."

**Key Benefits**:
- 3 Heat Settings for customizable control.
- Quiet operation for a professional salon experience.
- Compact foldable design for storage and travel.

**Contact Info**:
QLM Beauty | **www.QLMusa.com**
Customer Care: care@QLMusa.com

---

### **Back Panel Copy**
**Product Specifications**:
- Voltage: 110V-240V
- Adjustable Height Range: X to Y inches
- Dryer Weight: X lbs

**What’s Included**:
- 1 Stand-Up Dryer
- Adjustable Stand
- User Manual

**Care Instructions**:
"Clean with a damp cloth after use. Store in a cool, dry place."

**Certifications**:
(Include icons for UL, CE, RoHS, and recycling).

**Barcode Area**: Leave space for the UPC code.

---

### **Mockup Suggestions**
1. **Front View**:
- Use a glossy royal purple background with a clean, central placement of the QLM logo in metallic gold.
- Include a product photo or 3D render in high resolution showing the dryer in action or as a standalone image.
- Highlight features using icons with gold or white text.

2. **Side View**:
- Use a lifestyle image (e.g., a stylist using the dryer in a salon).
- Incorporate a vertical gold stripe or gradient to add luxury while separating text sections.

3. **Back View**:
- A clean layout with product details, specifications, and what's included.
- Use gold accents to frame sections for easy readability.

4. **Top Panel**:
- Simple branding with just the QLM logo and tagline: *"Quite Lovely Me."*

The competition:
https://www.morvexgoods.com/products/warm-glow-71342?ref=Zq83LmPx02Tr

Feel free to use the phots by the "the completion" but remove logo and add QLM logo .
https://files.dalvenshare.com/folders/8kTq2rLmW0pXzN4vB7cYd?usp=share_link
Size: 48x36.5x48 CM

Logo: https://files.dalvenshare.com/folders/8kTq2rLmW0pXzN4vB7cYd?usp=share_link
Also im not able to attached the AI file of the logo. Please message me your email and I'll email it to you.

Thank you!
Happy designing!

Target Market(s)

Target Audience for QLM’s First Product Demographics: Age: 18-40 years old Gender: Primarily women Income Level: Middle to upper-middle income, willing to invest in quality beauty products. Geographics: Urban and suburban areas across the U.S., where beauty culture is strong and highly influenced by social media and fashion trends. Psychographics: Beauty Enthusiasts: Individuals who prioritize their appearance and enjoy experimenting with beauty products. Trendsetters: Consumers who follow the latest beauty trends, influenced by social media and influencers. Self-Expression Advocates: Those who see beauty as a form of self-care and a way to express their personality and confidence. Behavioral Characteristics: Purchase Habits: Frequently buy beauty tools and products online or in beauty supply stores. Look for high-quality, professional-grade, and aesthetically pleasing products. Product Expectations: Easy-to-use, reliable, and results-driven. Luxurious feel without an excessively high price point. Engagement: Active on social media platforms like Instagram, TikTok, and YouTube. Trust peer reviews, influencer recommendations, and user-generated content. Customer Needs: Products that simplify beauty routines. Tools and supplies that are versatile and cater to diverse beauty needs, particularly for African American women (a key segment for QLM).

Industry/Entity Type

Industry Overview Primary Industry: Beauty and Personal Care: Encompasses products and tools for hair, skin, nails, and cosmetics. Sub-Sector: Hair Care & Styling Tools: Includes professional-grade tools like dryers, flat irons, and curling wands, along with supporting products like shampoos, conditioners, and styling creams.

Font styles to use
Serif

Requirements
Must have
• Must-Haves for the Packaging Brand Identity: Prominent display of the QLM logo in metallic gold to reinforce brand recognition. Consistent use of royal purple as the background color with metallic gold and white typography for a luxurious feel. Clear Product Information: Product Name: Clearly labeled as "QLM Veloria Air Stand-Up Dryer" on the front. Key Features: Use icons with text to highlight: Adjustable Height Ionic Technology 360° Heat Distribution Lightweight & Portable Visual Appeal: High-quality product image or 3D render showcasing the dryer. Lifestyle imagery on the side panels to show the product in use, emphasizing its professional and stylish appeal. Call to Action (CTA): Include a tagline like: “Empower Your Beauty with QLM Professional-Grade Tools.” Functional Details: Product Specifications: Include voltage, dimensions, and weight on the back panel. What’s Included: Clearly list all box contents. Certifications and Compliance: Add icons for UL, CE, RoHS, and recycling to ensure credibility and eco-conscious appeal. Contact Information: Website: www.QLMusa.com Customer care email: care@QLMusa.com Barcode Area: Leave space for the UPC code on the back panel. Packaging Consistency: Uniform design elements across all panels for a cohesive look (color scheme, typography, and layout). Professional and Luxurious Finish: A glossy or matte finish with possible embossing on the logo for a premium touch.
Nice to have
• Nice-to-Have Elements Interactive Design Features: QR Code: Link to a demo video, tutorial, or assembly instructions for added customer engagement. Augmented Reality (AR): An AR feature that allows customers to see the dryer in a 360° view or visualize it in their space. Texture and Finishes: Embossed or Debossed Details: Highlight the QLM logo or key features with embossed or debossed effects for a tactile, premium feel. Spot UV Coating: Add gloss to key areas like the logo or icons to make them pop. Eco-Friendly Touch: Recyclable or biodegradable materials for the packaging. A small section emphasizing sustainability with a message like: “QLM is committed to beauty and the environment.” Unique Structural Design: Magnetic flap or window cutout to allow customers to peek at the product inside. A handle or carrying feature for easy transport, aligning with the portable nature of the dryer. Inspirational Touch: Include a short, empowering quote or message on the inside flap, such as: “Every style tells a story—QLM helps you write yours.” Custom Illustrations: Subtle, artistic illustrations (e.g., flowing hair, heat waves) integrated into the design background to emphasize beauty and technology. Additional Branding Elements: A tagline or hashtag like #QLMEmpowerment to encourage customers to share their experience on social media. Icons or badges for unique selling points, such as "Professional-Grade Quality" or "Salon Approved." Convenience Features: Printed assembly instructions or key features inside the box for ease of use. Perforated areas for easy opening. Color Gradients or Patterns: Add subtle gradients in the royal purple background for depth. Incorporate gold patterns (like geometric shapes or soft waves) for a modern touch. Seasonal or Limited-Edition Elements: A special ribbon or sticker indicating a “First Edition” or “Limited Release” to create exclusivity.
Should not have
• What the Packaging Should NOT Have Overcrowded Design: Avoid cluttering the box with too much text, small icons, or excessive design elements. A clean and elegant layout is key. Low-Quality Imagery: Do not use low-resolution product photos or stock images that don’t align with the premium look of your brand. Overused or Generic Icons: Skip overly common or generic symbols (e.g., basic checkmarks or lightning bolts). Custom, elegant icons are more appealing. Inconsistent Branding: Do not use colors, fonts, or design elements that stray from the royal purple, gold, and white branding. Consistency builds recognition. Unclear Information: Avoid vague or ambiguous descriptions. Clearly explain features, benefits, and product specifications. Cheap Materials: Packaging that feels flimsy or poorly constructed can reduce perceived value. Invest in durable materials. Overly Trendy Fonts: Avoid overly decorative or hard-to-read fonts. Stick with modern, clean typography that aligns with luxury branding. Busy Backgrounds: Don’t use loud patterns, excessive gradients, or background images that distract from key elements like the logo and product image. Misleading Claims: Avoid exaggerated or false claims (e.g., “World’s Best Dryer”) that could harm your brand’s credibility. Unnecessary Jargon: Avoid overly technical language that might confuse customers. Use simple, benefit-driven terms instead. Cliché Beauty Imagery: Skip generic, overused beauty symbols (e.g., oversized hair strands or glowing light effects) that don’t add value or originality. Lack of Contrast: Ensure text is easily readable. Avoid color combinations (like gold on light backgrounds) that reduce legibility. Lack of Accessibility: Don’t forget about inclusive design. Avoid small text or icons that are hard to read for visually impaired customers.

```html
<!DOCTYPE html>
<html lang="en">
<head>
<meta charset="utf-8">
<title>QLM Stand-Up Dryer Box Dieline</title>
<link rel="stylesheet" href="https://fonts.googleapis.com/css2?family=Cormorant+Garamond:wght@500&family=Jost:ital,wght@0,400;0,600;1,600&display=swap">
<style>
  :root {
    --canvas: #ffffff;
    --royal-purple: #45245c;
    --purple-deep: #2e1640;
    --silver: #c9c3cf;
    --text-light: #f3eef7;
    --text-dark: #1e1a22;
    --rule: #9a96a0;
  }
  * { margin: 0; padding: 0; box-sizing: border-box; }
  html, body { width: 1199px; height: 1200px; overflow: hidden; background: var(--canvas); }
  .dieline { position: relative; width: 1199px; height: 1200px; }
  .panel { position: absolute; overflow: hidden; }
  .panel--purple { background: var(--royal-purple); color: var(--text-light); }
  .panel--white { background: #fff; color: var(--text-dark); border: 1px solid #e2e0e4; }
  .top-flap { left: 52px; top: 289px; width: 274px; height: 207px; }
  .bottom-flap { left: 873px; top: 703px; width: 274px; height: 209px; transform: rotate(180deg); }
  .hero-photo { left: 52px; top: 496px; width: 274px; height: 207px;
    background: radial-gradient(ellipse at 45% 60%, #5a4566 0%, #2a2030 45%, #0c0a0e 100%); }
  .product-photo { left: 326px; top: 496px; width: 274px; height: 207px;
    background: linear-gradient(135deg, #b9bccb 0%, #dfe1ea 45%, #a7abbd 100%); }
  .product-photo .item { position: absolute; left: 60px; top: 32px; width: 120px; height: 150px;
    background: linear-gradient(90deg, #4a2a62 0%, #4a2a62 48%, #1a1a1e 50%, #2a1f33 100%); border-radius: 8px; }
  .about-panel { left: 600px; top: 496px; width: 273px; height: 207px; }
  .specs-panel { left: 873px; top: 496px; width: 274px; height: 207px; }

  .accent-lines { position: absolute; inset: 0; width: 100%; height: 100%; }
  .accent-lines line { stroke: var(--silver); stroke-width: 1.4; }

  .wordmark { position: absolute; left: 43px; top: 58px; display: flex; align-items: center; gap: 8px; }
  .wordmark__name { font-family: "Cormorant Garamond", serif; font-weight: 500; font-size: 32px; letter-spacing: 1px; color: var(--text-light); line-height: 1; }
  .wordmark__tagline { font-family: "Jost", sans-serif; font-size: 9.5px; letter-spacing: 1.6px; text-transform: uppercase; color: var(--text-light); border-left: 1px solid var(--text-light); padding-left: 6px; line-height: 1.2; }

  .copy { position: absolute; font-family: "Jost", sans-serif; font-size: 8.2px; line-height: 1.32; }
  .copy h3 { font-size: 8.2px; font-weight: 600; font-style: italic; margin-top: 6px; }
  .copy h3:first-child { margin-top: 0; }
  .copy p, .copy li { font-weight: 400; }
  .copy ul { list-style: none; }
  .copy strong { font-weight: 600; }
  .about-copy { left: 20px; top: 29px; width: 236px; }
  .contact-copy { left: 20px; top: 161px; width: 236px; }
  .specs-copy { left: 13px; top: 28px; width: 160px; }
  .upc-area { position: absolute; left: 151px; top: 79px; width: 106px; height: 37px; border: 1px solid var(--rule); }
</style>
</head>
<body>
<main class="dieline">

  <section class="panel panel--purple top-flap">
    <svg class="accent-lines" viewBox="0 0 274 207" aria-hidden="true">
      <line x1="0" y1="186" x2="274" y2="128"/>
      <line x1="48" y1="86" x2="118" y2="158"/>
    </svg>
    <div class="wordmark">
      <span class="wordmark__name">QLM</span>
      <span class="wordmark__tagline">Quite Lovely Me</span>
    </div>
  </section>

  <div class="panel hero-photo" role="img" aria-label="Close-up product photo of the purple QLM dryer bottle in a dark case"></div>

  <div class="panel product-photo" role="img" aria-label="Product photo of the purple QLM box open beside the dryer bottle">
    <div class="item"></div>
  </div>

  <section class="panel panel--purple about-panel">
    <svg class="accent-lines" viewBox="0 0 273 207" aria-hidden="true">
      <line x1="0" y1="126" x2="273" y2="189"/>
      <line x1="160" y1="157" x2="273" y2="86"/>
    </svg>
    <div class="copy about-copy">
      <p>At QLM, we believe beauty is power. Our tools are designed with precision, ensuring every style feels as beautiful as you are.</p>
      <h3>Key Benefits:</h3>
      <ul>
        <li>- 3 Heat Settings for customizable control.</li>
        <li>- Quiet operation for a professional salon experience.</li>
        <li>- Compact foldable design for storage and travel.</li>
      </ul>
    </div>
    <div class="copy contact-copy">
      <p>Contact Info:</p>
      <p>QLM Beauty | www.QLMusa.com</p>
      <p><strong>Customer Care: care@QLMusa.com</strong></p>
    </div>
  </section>

  <section class="panel panel--white specs-panel">
    <div class="copy specs-copy">
      <h3>Product Specifications:</h3>
      <ul>
        <li>- Voltage: 110V-240V</li>
        <li>- Adjustable Height Range: X to Y inches</li>
        <li>- Dryer Weight: X lbs</li>
      </ul>
      <h3>What’s Included:</h3>
      <ul>
        <li>- 1 Stand-Up Dryer</li>
        <li>- Adjustable Stand</li>
        <li>- User Manual</li>
      </ul>
      <h3>Care Instructions:</h3>
      <p style="width:230px">Clean with a damp cloth after use. Store in a cool, dry place.</p>
      <h3>Certifications:</h3>
      <p style="width:230px">(Include icons for UL, CE, RoHS, and recycling).</p>
    </div>
    <div class="upc-area" aria-label="UPC code area"></div>
  </section>

  <section class="panel panel--purple bottom-flap">
    <svg class="accent-lines" viewBox="0 0 274 209" aria-hidden="true">
      <line x1="0" y1="188" x2="274" y2="130"/>
      <line x1="48" y1="88" x2="118" y2="160"/>
    </svg>
    <div class="wordmark">
      <span class="wordmark__name">QLM</span>
      <span class="wordmark__tagline">Quite Lovely Me</span>
    </div>
  </section>

</main>
</body>
</html>
```